Business Card for Graphic Design Firm

This project is for a new graphic design firm based in New Jersey called Velmoth. We outsource graphic design and marketing jobs. We want to communicate that this is a professional company but it as well creative and artistic. This card may be used as a horizontal double sided paper card or a vertical single sided translucent card so feel free to submit designs in whichever format or both.
Updates

Reason: Extending the deadline because I'm not exactly satisfied with the designs so far.

Please view the updated project brief

Target Market(s)

Adults aged 25-60

Industry/Entity Type

Graphic Design

Font styles to use
Serif
Sans Serif

Requirements
Nice to have
• Maybe a triangular pattern around the edges similar to our logo

```html
<!DOCTYPE html>
<html lang="en">
<head>
<meta charset="utf-8">
<title>Velmoth Business Card</title>
<link rel="stylesheet" href="https://fonts.googleapis.com/css2?family=Source+Sans+3:wght@400;600;700&display=swap">
<style>
  :root {
    --backdrop: #e9e8e6;
    --card: #ffffff;
    --ink-grey: #6d6e70;
    --ink-text: #6a6a6a;
    --brand-teal: #126f8e;
    --accent-teal: #1b85a6;
    --rule: #9a9a9a;
    --tone-navy: #0d7392;
    --tone-teal: #0ba5bb;
    --tone-sky: #7fcfea;
    --tone-slate: #6c7374;
    --tone-amber: #f7b21c;
    --tone-orange: #f2831f;
  }
  * { margin: 0; padding: 0; box-sizing: border-box; }
  html, body { width: 1200px; height: 1000px; overflow: hidden; }
  body {
    background: var(--backdrop);
    font-family: "Source Sans 3", Arial, sans-serif;
    position: relative;
  }
  .card {
    position: absolute;
    left: 265px;
    width: 665px;
    height: 397px;
    background: var(--card);
    overflow: hidden;
    box-shadow: 0 2px 6px rgba(0,0,0,0.18);
  }
  .card--front { top: 73px; }
  .card--back { top: 532px; }

  .pattern-area {
    position: absolute;
    top: 0;
    right: 0;
    width: 392px;
    height: 397px;
    background:
      linear-gradient(200deg, var(--tone-navy) 0%, var(--tone-teal) 30%, var(--tone-sky) 50%, rgba(255,255,255,0) 68%),
      linear-gradient(300deg, var(--tone-orange) 0%, var(--tone-amber) 22%, rgba(255,255,255,0) 45%),
      linear-gradient(45deg, var(--tone-slate) 0%, rgba(108,115,116,0.6) 20%, #ffffff 45%);
  }
  .pattern-area--faint { opacity: 0.28; }

  .wordmark {
    position: absolute;
    color: var(--ink-grey);
    font-weight: 600;
    letter-spacing: 0.06em;
    line-height: 1;
  }
  .card--front .wordmark { left: 33px; top: 330px; font-size: 42px; }
  .card--back .wordmark { left: 358px; top: 334px; font-size: 34px; }

  .identity {
    position: absolute;
    left: 33px;
    top: 98px;
    width: 185px;
    text-align: right;
  }
  .identity__name {
    color: var(--brand-teal);
    font-weight: 700;
    font-size: 37px;
    line-height: 1;
  }
  .identity__role {
    color: var(--accent-teal);
    font-size: 17px;
    line-height: 1.1;
  }
  .divider {
    position: absolute;
    left: 235px;
    top: 100px;
    width: 1px;
    height: 98px;
    background: var(--rule);
  }
  .contact {
    position: absolute;
    left: 252px;
    top: 102px;
    list-style: none;
    color: var(--ink-text);
    font-size: 17px;
    line-height: 24.5px;
  }
  .contact li { display: flex; align-items: flex-start; }
  .contact svg { width: 15px; height: 15px; margin: 4px 9px 0 0; flex: none; fill: var(--accent-teal); }
  .contact .spacer { width: 15px; margin-right: 9px; flex: none; }
</style>
</head>
<body>
  <section class="card card--front">
    <div class="pattern-area" role="img" aria-label="Triangular pattern in navy, teal, sky blue, slate grey, amber and orange"></div>
    <div class="wordmark">VELMOTH</div>
  </section>

  <section class="card card--back">
    <div class="pattern-area pattern-area--faint" role="img" aria-label="Faint triangular pattern in pale blue, grey and peach"></div>
    <div class="identity">
      <div class="identity__name">Mara Lind</div>
      <div class="identity__role">Manager / CEO</div>
    </div>
    <div class="divider"></div>
    <ul class="contact">
      <li><svg viewBox="0 0 16 16"><path d="M2 6c0-2 3-3 6-3s6 1 6 3v1h-3V5.5H5V7H2z"/><rect x="3" y="8" width="10" height="6" rx="1"/></svg>+61 3 9000 4127</li>
      <li><svg viewBox="0 0 16 16"><path d="M1 3h14v10H1z"/><path d="M1 3l7 6 7-6" fill="none" stroke="#fff" stroke-width="1.4"/></svg>info@velmoth.com</li>
      <li><svg viewBox="0 0 16 16"><circle cx="8" cy="8" r="7"/><path d="M1 8h14M8 1c-3 3-3 11 0 14M8 1c3 3 3 11 0 14" fill="none" stroke="#fff" stroke-width="1"/></svg>www.velmoth.com</li>
      <li><svg viewBox="0 0 16 16"><path d="M8 1a5 5 0 0 1 5 5c0 4-5 9-5 9S3 10 3 6a5 5 0 0 1 5-5z"/><circle cx="8" cy="6" r="2" fill="#fff"/></svg>14 Calder Lane</li>
      <li><span class="spacer"></span>Norwood VIC 3081</li>
    </ul>
    <div class="wordmark">VELMOTH</div>
  </section>
</body>
</html>
```